Business card for a boutique travel agency VELARIEN

we need a business card design - double sided. We would like to have a very elegant, sophisticated but modern design. we are travel consultants and our business focus is Europe, mainly the city of Paris. We would like to receive designs in white and silver, black color but if you are confident that we should pick up a color to make it different and more beautful...go ahead! We are going to give business cards to our clients and business partners. It is important to be perceived as elegant, modern and trustful. Please check jpg references.

Target Market(s)

Velarien primary clients are individuals, couples and affinity groups of high-net-worth who travel for leisure at least once per year. Seeking the ultimate travel experience, the target clients demand the finest quality activities and accommodations accompanied by a superior level of service.

Industry/Entity Type

Travel Industry

Contact Information for Business Card

Lucinda Farrow
- lucinda@velarien-example.com
- +55 11 98347.2516
- velarien-example.com
- unique travel experiences (we would like to see this signature printed as a detail)

Font styles to use
Sans Serif

Colors

Designer to choose colors to be used in the design.

Requirements
Must have
• the Velarien logo that I have attached
Nice to have
• we would like to have some nice detail, something different that shows that we care about,... we are detail oriented.
Should not have
• decorative fonts

```html
<!DOCTYPE html>
<html lang="en">
<head>
<meta charset="utf-8">
<title>Velarien — Business Card</title>
<link rel="stylesheet" href="https://fonts.googleapis.com/css2?family=Titillium+Web:wght@300;400&display=swap">
<style>
  :root {
    --backdrop: #b9b9b9;
    --paper: #ffffff;
    --ink: #1a1a1a;
    --card-black: #0b0b0c;
    --silver: #d4d4d4;
    --frame-dark: #3a3a3a;
  }
  * { box-sizing: border-box; margin: 0; padding: 0; }
  html, body {
    width: 1200px;
    height: 1200px;
    overflow: hidden;
  }
  body {
    background: var(--backdrop);
    font-family: "Titillium Web", Arial, sans-serif;
    display: flex;
    flex-direction: column;
    align-items: center;
    justify-content: center;
    gap: 80px;
  }
  .card {
    position: relative;
    width: 760px;
    height: 440px;
    box-shadow: 0 6px 18px rgba(0,0,0,0.18);
  }
  .card__frame {
    position: absolute;
    inset: 30px;
    border: 1px solid var(--frame-dark);
  }
  .card__frame::after {
    content: "";
    position: absolute;
    inset: 6px;
    border: 1px solid var(--frame-dark);
  }

  /* Front: contact side */
  .card--front {
    background: var(--paper);
    color: var(--ink);
  }
  .contact {
    position: absolute;
    inset: 0;
    display: flex;
    flex-direction: column;
    align-items: center;
    text-align: center;
  }
  .contact__name {
    margin-top: 128px;
    font-weight: 300;
    font-size: 34px;
    letter-spacing: 0.5px;
    text-transform: uppercase;
    line-height: 1;
  }
  .contact__tagline {
    margin-top: 10px;
    font-weight: 300;
    font-size: 15px;
    letter-spacing: 0.3px;
  }
  .contact__details {
    margin-top: 72px;
    font-weight: 300;
    font-size: 18px;
    line-height: 1.9;
  }

  /* Back: brand side */
  .card--back {
    background: var(--card-black);
    color: var(--paper);
  }
  .card--back .card__frame,
  .card--back .card__frame::after {
    border-color: var(--silver);
  }
  .brand {
    position: absolute;
    inset: 0;
    display: flex;
    align-items: center;
    justify-content: center;
  }
  .brand__name {
    font-weight: 300;
    font-size: 46px;
    letter-spacing: 20px;
    padding-left: 20px;
    text-transform: uppercase;
  }
</style>
</head>
<body>
  <section class="card card--front" aria-label="Business card front">
    <div class="card__frame"></div>
    <div class="contact">
      <h1 class="contact__name">Lucinda Farrow</h1>
      <p class="contact__tagline">unique travel experiences</p>
      <p class="contact__details">
        T: +55 11 98347.2516<br>
        W: velarien-example.com | E: lucinda@velarien-example.com
      </p>
    </div>
  </section>

  <section class="card card--back" aria-label="Business card back">
    <div class="card__frame"></div>
    <div class="brand">
      <span class="brand__name">Velarien</span>
    </div>
  </section>
</body>
</html>
```